Power Point Presentation to Large Audience

Make a consistent look and feel but also make it a compelling presentation. I have attached a summary of my presentation

Target Market(s)

I am making a presentation to investors. Need a consistent look feel but I need it to be simple in design

Requirements
Must have
• Use http://brightlane4jobs.example/ for any background into the company
Nice to have
• My presentation has to be short, less than 10 to 15 minutes. The format I have attached is my basic content, I need it cleaned up and put in a compelling format

```html
<!DOCTYPE html>
<html lang="en">
<head>
<meta charset="utf-8">
<title>BrightLane4Jobs Investor Deck — Second Part</title>
<link href="https://fonts.googleapis.com/css2?family=Roboto:wght@400;500;700;900&display=swap" rel="stylesheet">
<style>
:root{
  --orange:#f7941d;
  --ink:#333333;
  --grey-band:#767171;
  --canvas:#ebebeb;
  --white:#ffffff;
  --dark:#262626;
  --rule:#e2e2e2;
}
*{box-sizing:border-box;margin:0;padding:0}
html,body{width:1200px;height:1200px;overflow:hidden;background:var(--canvas);font-family:"Roboto",Arial,sans-serif;color:var(--ink)}
.board{position:relative;width:1200px;height:1200px}
.slide{position:absolute;background:var(--white);overflow:hidden}
.col-left{left:19px;width:573px}
.col-right{left:610px;width:571px}
.row-1{top:22px;height:322px}
.row-2{top:362px;height:323px}
.row-3{top:702px;height:323px}
.accent{color:var(--orange)}
.brand{position:absolute;top:18px;right:20px;font-size:9px;font-weight:700;color:var(--orange);letter-spacing:.2px}
.footer{position:absolute;left:0;right:0;bottom:0;height:18px;display:flex}
.footer-band{flex:0 0 474px;background:var(--grey-band);color:#eee;font-size:5.5px;line-height:18px;padding-left:18px;white-space:nowrap}
.footer-mark{flex:0 0 61px;display:flex;align-items:center;justify-content:center;gap:3px;font-size:9px;color:#666;font-weight:400}
.footer-mark i{width:6px;height:6px;background:var(--orange);display:block}
.footer-page{flex:1;background:var(--orange);color:#fff;font-size:5.5px;line-height:18px;padding-left:14px}
.title{position:absolute;left:18px;top:20px;font-size:17px;font-weight:700;line-height:19px;color:var(--ink);letter-spacing:.2px}
.photo{position:absolute}
.ring{position:absolute;border:1.6px solid var(--orange);border-radius:50%;display:flex;align-items:center;justify-content:center}
.label{position:absolute;text-align:center;font-weight:700;color:var(--orange);font-size:14px;line-height:18px}
.divider{position:absolute;width:1px;background:var(--rule)}
.part-heading{position:absolute;left:20px;top:1088px;font-size:60px;font-weight:900;color:#111;letter-spacing:.5px}
</style>
</head>
<body>
<div class="board">

  <!-- Slide: the disconnect -->
  <section class="slide col-left row-1">
    <svg style="position:absolute;left:23px;top:75px" width="62" height="62" viewBox="0 0 62 62" fill="none" stroke="#f7941d" stroke-width="3" stroke-linecap="round">
      <path d="M34 14 l8-8 a9 9 0 0 1 13 13 l-8 8"/>
      <path d="M28 48 l-8 8 a9 9 0 0 1-13-13 l8-8"/>
      <path d="M18 4v8M4 18h8M44 50v8M50 44h8M8 8l5 5M49 49l5 5"/>
    </svg>
    <div style="position:absolute;left:18px;top:154px;font-size:22px;line-height:27px;color:#444">What is<br>the <span class="accent" style="font-weight:700">disconnect?</span></div>
    <div class="photo" style="left:273px;top:0;width:8px;height:322px;background:#8a8a8a"></div>
    <div class="photo" role="img" aria-label="Photo of a discouraged teenage student sitting on worn stone steps beside a backpack, holding a blue book" style="left:281px;top:0;width:292px;height:322px;background:linear-gradient(160deg,#a0704f 0%,#8c7f73 35%,#3c4a66 60%,#6e6a62 100%)"></div>
  </section>

  <!-- Slide: statistic -->
  <section class="slide col-right row-1">
    <div class="photo" role="img" aria-label="Close-up photo of a child's hand drawing with pink chalk on pavement" style="left:0;top:0;width:246px;height:322px;background:linear-gradient(135deg,#9b8d86 0%,#b58f8f 45%,#c2485f 75%,#8f8480 100%)"></div>
    <div class="brand">BrightLane4Jobs</div>
    <div class="ring" style="left:372px;top:72px;width:76px;height:76px">
      <svg width="42" height="42" viewBox="0 0 42 42" fill="none" stroke="#444" stroke-width="1.6"><circle cx="21" cy="15" r="10"/><path d="M4 40c2-9 9-13 17-13s15 4 17 13"/></svg>
    </div>
    <p style="position:absolute;left:290px;top:158px;width:240px;text-align:center;font-size:13.5px;line-height:17.3px;color:#333">Less than <b class="accent">10 percent</b> of children born in the bottom quartile of household incomes attain a bachelor’s degree by age 25, compared to <b class="accent">more than 50 percent</b> in the top quartile.</p>
    <div class="footer"><div class="footer-band" style="padding-left:18px">EduNorth™ &nbsp;BrightLane4Jobs™ &nbsp;&nbsp;2018 Trademark EduNorth, LLC</div><div class="footer-mark"><i></i>EduNorth</div><div class="footer-page">8</div></div>
  </section>

  <!-- Slide: three areas -->
  <section class="slide col-left row-2">
    <h2 class="title">Disconnect between Education to the Realities<br>of Employment</h2>
    <div class="brand">BrightLane4Jobs</div>
    <div class="divider" style="left:195px;top:90px;height:172px"></div>
    <div class="divider" style="left:378px;top:90px;height:172px"></div>

    <div class="ring" style="left:64px;top:116px;width:76px;height:76px">
      <svg width="44" height="36" viewBox="0 0 44 36" fill="none" stroke="#444" stroke-width="1.6" stroke-linejoin="round"><path d="M2 12 22 3 42 12 22 21Z"/><path d="M10 16v10c6 6 18 6 24 0V16"/><path d="M38 14v10"/></svg>
    </div>
    <div class="label" style="left:40px;top:208px;width:124px">Education</div>

    <div class="ring" style="left:248px;top:116px;width:76px;height:76px">
      <svg width="40" height="46" viewBox="0 0 40 46" fill="none" stroke="#444" stroke-width="1.6" stroke-linejoin="round"><path d="M20 3l-3 4 3 3 3-3z"/><path d="M18 10l-3 16 5 5 5-5-3-16"/><path d="M2 32h8l8 4h10c3 0 3 4 0 4H18"/><path d="M2 44h12l10 0 14-10c2-2 0-5-3-4l-9 5"/></svg>
    </div>
    <div class="label" style="left:224px;top:208px;width:124px">Employment</div>

    <div class="ring" style="left:432px;top:116px;width:76px;height:76px">
      <svg width="44" height="40" viewBox="0 0 44 40" fill="none" stroke="#444" stroke-width="1.6"><path d="M3 2v36h39"/><path d="M9 36V24M16 36V20M23 36V24M30 36V16M37 36V12"/><path d="M8 20l8-7 7 5 13-12"/><path d="M31 6h5v5"/></svg>
    </div>
    <div class="label" style="left:396px;top:208px;width:148px">Economic<br>Development</div>

    <div class="footer"><div class="footer-band">EduNorth™ &nbsp;BrightLane4Jobs™ &nbsp;&nbsp;2018 Trademark EduNorth, LLC</div><div class="footer-mark"><i></i>EduNorth</div><div class="footer-page">9</div></div>
  </section>

  <!-- Slide: solution -->
  <section class="slide col-right row-2">
    <h2 class="title" style="top:30px">The BrightLane 4 Jobs Solution</h2>
    <div class="brand">BrightLane4Jobs</div>
    <div class="photo" role="img" aria-label="3D illustration of orange figures on a platform linked by a jigsaw-piece bridge to white figures on a higher platform" style="left:285px;top:54px;width:286px;height:251px;background:radial-gradient(ellipse at 70% 40%,#f4f4f4 0%,#e3e3e3 55%,#ffffff 100%)">
      <div style="position:absolute;left:40px;top:135px;width:90px;height:90px;border-radius:40%;background:radial-gradient(circle,#f7b21d 0%,#f0a010 60%,transparent 62%)"></div>
    </div>
    <div style="position:absolute;left:18px;top:107px;font-size:12px;font-weight:500;color:#333">Education + Industry</div>
    <svg style="position:absolute;left:18px;top:131px" width="16" height="16" viewBox="0 0 16 16" fill="none" stroke="#f7941d" stroke-width="1.2"><circle cx="8" cy="8" r="7"/><path d="M4.5 8.2l2.3 2.3 4.5-4.8"/></svg>
    <p style="position:absolute;left:42px;top:129px;width:240px;font-size:10px;line-height:13px;color:#333">We connect education and industry to assist and motivate students to achieve employment success.</p>
    <div style="position:absolute;left:18px;top:204px;font-size:12px;font-weight:500;color:#333">BrightLane4Jobs</div>
    <svg style="position:absolute;left:18px;top:228px" width="16" height="16" viewBox="0 0 16 16" fill="none" stroke="#f7941d" stroke-width="1.2"><circle cx="8" cy="8" r="7"/><path d="M4.5 8.2l2.3 2.3 4.5-4.8"/></svg>
    <p style="position:absolute;left:42px;top:226px;width:230px;font-size:10px;line-height:13px;color:#333">BL4J offers the bridge between education and industry that can help educators and students connect with the opportunities in their local job market</p>
    <div class="footer"><div class="footer-band">EduNorth™ &nbsp;BrightLane4Jobs™ &nbsp;&nbsp;2018 Trademark EduNorth, LLC</div><div class="footer-mark"><i></i>EduNorth</div><div class="footer-page">10</div></div>
  </section>

  <!-- Slide: mission -->
  <section class="slide col-left row-3">
    <h2 class="title" style="top:33px">The BL4J Mission</h2>
    <div class="brand">BrightLane4Jobs</div>
    <div role="img" aria-label="Dark background photo of a compass" style="position:absolute;left:0;top:66px;width:573px;height:101px;background:linear-gradient(110deg,#1e1e1e 0%,#3a3a3a 45%,#222 100%)"></div>
    <p style="position:absolute;left:20px;top:93px;width:533px;text-align:center;color:#fff;font-size:14.2px;line-height:17.3px">The mission of <span class="accent" style="font-weight:500">BrightLane4Jobs</span> is to promote education with destination through the creation of high-quality tools and resources that enhance the intersection of educational practices with <b class="accent">high-value career opportunities.</b></p>
    <div style="position:absolute;left:0;width:573px;top:178px;text-align:center;font-size:12px;font-weight:500;color:#333">Our Goal is to Assist Students in Becoming</div>
    <div class="divider" style="left:195px;top:208px;height:92px"></div>
    <div class="divider" style="left:378px;top:208px;height:92px"></div>

    <div class="ring" style="left:79px;top:216px;width:46px;height:46px">
      <svg width="26" height="26" viewBox="0 0 26 26" fill="none" stroke="#444" stroke-width="1.3"><circle cx="13" cy="9" r="6"/><path d="M3 25c1-6 5-9 10-9s9 3 10 9"/><path d="M13 16v5"/></svg>
    </div>
    <div class="label" style="left:52px;top:271px;width:100px;font-size:12px">Career-Ready</div>

    <div class="ring" style="left:263px;top:216px;width:46px;height:46px">
      <svg width="26" height="28" viewBox="0 0 26 28" fill="none" stroke="#444" stroke-width="1.3"><path d="M13 6a7 7 0 0 0-4 13v3h8v-3a7 7 0 0 0-4-13z"/><path d="M10 25h6M13 1v2M3 5l2 2M23 5l-2 2M1 13h2M23 13h2"/></svg>
    </div>
    <div class="label" style="left:236px;top:271px;width:100px;font-size:12px">Career-Wise</div>

    <div class="ring" style="left:451px;top:216px;width:46px;height:46px">
      <svg width="30" height="24" viewBox="0 0 30 24" fill="none" stroke="#444" stroke-width="1.3" stroke-linejoin="round"><path d="M1 6l5-3 5 2 5-2 4 2"/><path d="M29 6l-5-3M1 6l5 10 4 4c2 2 4 1 4-1l2 2c2 1 4-1 3-2l1 0c2 0 3-2 2-3l-1-1c2 0 2-2 1-3L24 3"/><path d="M11 5l-3 4c-1 2 2 3 3 1l3-3"/></svg>
    </div>
    <div class="label" style="left:414px;top:271px;width:120px;font-size:12px">Career-Engaged</div>

    <div class="footer"><div class="footer-band">EduNorth™ &nbsp;BrightLane4Jobs™ &nbsp;&nbsp;2018 Trademark EduNorth, LLC</div><div class="footer-mark"><i></i>EduNorth</div><div class="footer-page">11</div></div>
  </section>

  <!-- Slide: current successes -->
  <section class="slide col-right row-3">
    <h2 class="title" style="top:33px">Current Successes</h2>
    <div class="brand">BrightLane4Jobs</div>
    <ul style="list-style:none;position:absolute;left:24px;top:68px">
      <li style="display:flex;align-items:center;gap:10px;height:35.4px;font-size:15.5px;font-weight:700;color:#444"><svg width="16" height="16" viewBox="0 0 16 16" fill="none" stroke="#f7941d" stroke-width="1.2"><circle cx="8" cy="8" r="7"/><path d="M4.5 8.2l2.3 2.3 4.5-4.8"/></svg>Tennessee</li>
      <li style="display:flex;align-items:center;gap:10px;height:35.4px;font-size:15.5px;font-weight:700;color:#444"><svg width="16" height="16" viewBox="0 0 16 16" fill="none" stroke="#f7941d" stroke-width="1.2"><circle cx="8" cy="8" r="7"/><path d="M4.5 8.2l2.3 2.3 4.5-4.8"/></svg>New Mexico</li>
      <li style="display:flex;align-items:center;gap:10px;height:35.4px;font-size:15.5px;font-weight:700;color:#444"><svg width="16" height="16" viewBox="0 0 16 16" fill="none" stroke="#f7941d" stroke-width="1.2"><circle cx="8" cy="8" r="7"/><path d="M4.5 8.2l2.3 2.3 4.5-4.8"/></svg>West Virginia</li>
      <li style="display:flex;align-items:center;gap:10px;height:35.4px;font-size:15.5px;font-weight:700;color:#444"><svg width="16" height="16" viewBox="0 0 16 16" fill="none" stroke="#f7941d" stroke-width="1.2"><circle cx="8" cy="8" r="7"/><path d="M4.5 8.2l2.3 2.3 4.5-4.8"/></svg>Kentucky</li>
      <li style="display:flex;align-items:center;gap:10px;height:35.4px;font-size:15.5px;font-weight:700;color:#444"><svg width="16" height="16" viewBox="0 0 16 16" fill="none" stroke="#f7941d" stroke-width="1.2"><circle cx="8" cy="8" r="7"/><path d="M4.5 8.2l2.3 2.3 4.5-4.8"/></svg>Nebraska</li>
      <li style="display:flex;align-items:center;gap:10px;height:35.4px;font-size:15.5px;font-weight:700;color:#444"><svg width="16" height="16" viewBox="0 0 16 16" fill="none" stroke="#f7941d" stroke-width="1.2"><circle cx="8" cy="8" r="7"/><path d="M4.5 8.2l2.3 2.3 4.5-4.8"/></svg>Arkansas</li>
    </ul>
    <div class="photo" role="img" aria-label="Cover of a state employer skill-needs survey report with photos of workers" style="left:231px;top:52px;width:83px;height:107px;background:linear-gradient(180deg,#e9e9e9 0%,#2f4f8a 30%,#1f3d78 85%,#f0a010 100%);border-right:10px solid #b3123a"></div>
    <div class="photo" role="img" aria-label="Screenshot of the SBDA district data dashboard website" style="left:327px;top:52px;width:229px;height:107px;background:linear-gradient(180deg,#f4f4f4 0%,#e6e6e6 55%,#b64a3a 80%,#9a9a9a 100%)"></div>
    <div class="photo" role="img" aria-label="Screenshot of a New Mexico career website showing a red rock desert landscape" style="left:231px;top:169px;width:325px;height:129px;background:linear-gradient(180deg,#f6f6f6 0 7%,#2e4a78 7%,#6b7f9c 45%,#b5542b 72%,#5a3520 100%)"></div>
    <div class="footer"><div class="footer-band">EduNorth™ &nbsp;BrightLane4Jobs™ &nbsp;&nbsp;2018 Trademark EduNorth, LLC</div><div class="footer-mark"><i></i>EduNorth</div><div class="footer-page">12</div></div>
  </section>

  <h1 class="part-heading">SECOND PART</h1>
</div>
</body>
</html>
```